Film Poster Design For Japanese Film Poster #2

The title of this colour film is KAZE YAMA TSUKI HOSHI春 夏 秋 冬Translated this is literallySpring Summer Fall Winter ... however the English title is FOUR SEASONSWe attached a series of screen shots from the film and also the computer generated Kanji characters. We will be updating the brief with the Japanese title characters which currently being hand painted.We require the post in two formats. One being the traditional poster format and the other being in a wide screen ration of 1000px by 465px. Same design.This is a drama, feature length film comprising of four separate stories. The is mixture of Japanese and English dialogue. We are looking at 2 possible designs. You can choose to submit either.1: A with lots of white space ... focussing on smaller images at the Japanese text. I have uploaded a sample poster as a very rough indication. "Stories nobody ever wrote down about the quiet ones" / "Odile Bettina Rue Ingrid" - Lots of white space.Ideally we would have liked to have had the image of the young girl in the kimono pulling on the bell rope clear cut and used on white as a single main image. However, we are not sure that the clarity or resolution of the original image is sufficient. 2: One with lots of images as you can see with the two "Bridge Of Dust" Sample posters.Obviously we are not looking for a copy of either poster, but these posters are a guide to the two looks we are after.Thanks. Kaede
Hello all,Apologies for the delay. We have had to work through some naming issues.The film's English title has had to be renamed to THE LANTERNS. Please do not used TEN LANTERNS in any designed moving forward.Thanks Kaede Added Sunday, May 25, 2014

```html
<!DOCTYPE html>
<html lang="en">
<head>
<meta charset="utf-8">
<title>KAZE YAMA TSUKI HOSHI — Film Poster</title>
<link rel="stylesheet" href="https://fonts.googleapis.com/css2?family=Roboto:wght@300;400;700&family=Shippori+Mincho:wght@500&display=swap">
<style>
  :root {
    --ink: #000000;
    --paper: #ffffff;
    --mist: #c9c9c9;
    --credit: #e6e6e6;
    --t-green: #5fae4c;
    --t-orange: #e88a2a;
    --t-blue: #3c7fc4;
    --scene-top: #0a0706;
    --scene-mid: #2a221d;
    --scene-low: #5a564f;
    --scene-floor: #1c1b19;
  }
  * { margin: 0; padding: 0; box-sizing: border-box; }
  html, body { width: 800px; height: 1200px; overflow: hidden; background: var(--ink); }
  .poster {
    position: relative;
    width: 800px;
    height: 1200px;
    background: var(--ink);
    font-family: "Roboto", Arial, sans-serif;
    color: var(--paper);
    overflow: hidden;
  }
  .romaji-title {
    position: absolute;
    top: 42px;
    left: 0;
    width: 100%;
    text-align: center;
    font-size: 37px;
    font-weight: 300;
    letter-spacing: 2px;
    word-spacing: 4px;
  }
  .romaji-title strong { font-weight: 700; }

  .gate-scene {
    position: absolute;
    left: 0;
    top: 600px;
    width: 800px;
    height: 470px;
    background:
      radial-gradient(ellipse 60% 45% at 50% 60%, rgba(150,145,135,0.55), rgba(0,0,0,0) 70%),
      linear-gradient(to bottom, var(--scene-top) 0%, var(--scene-mid) 35%, var(--scene-low) 62%, var(--scene-floor) 85%, var(--ink) 100%);
  }

  .season-strips { position: absolute; left: 0; top: 0; width: 800px; height: 700px; }
  .strip { position: absolute; }
  .strip--one {
    left: 262px; top: 185px; width: 258px; height: 88px;
    border-radius: 6px 40px 30px 60px / 6px 30px 40px 30px;
    background: linear-gradient(100deg, #3c3f3e 0%, #8b8f86 40%, #4d6a3e 75%, #1d2a1a 100%);
  }
  .strip--two {
    left: 262px; top: 276px; width: 262px; height: 104px;
    border-radius: 20px 50px 40px 14px / 30px 40px 30px 20px;
    background: linear-gradient(to bottom, #2c2620 0%, #8a6b47 35%, #c99e6b 55%, #3a2e24 100%);
  }
  .strip--three {
    left: 268px; top: 400px; width: 258px; height: 140px;
    border-radius: 60px 20px 50px 30px / 50px 30px 40px 40px;
    background: linear-gradient(110deg, #3a1d10 0%, #8a3b1c 40%, #c2643a 60%, #4a2616 100%);
  }
  .strip--four {
    left: 262px; top: 542px; width: 250px; height: 128px;
    border-radius: 40px 60px 50px 20px / 30px 50px 60px 30px;
    background: linear-gradient(to bottom, #e6e8ea 0%, #9aa2a8 30%, #3a4446 65%, #7d8589 100%);
  }

  .kanji-title {
    position: absolute;
    left: 0;
    top: 0;
    width: 800px;
    height: 700px;
    font-family: "Shippori Mincho", "Noto Serif JP", serif;
    font-weight: 500;
    font-size: 80px;
    line-height: 100px;
    color: var(--paper);
  }
  .kanji-title span { position: absolute; left: 355px; width: 90px; text-align: center; }
  .kanji-title .k1 { top: 168px; }
  .kanji-title .k2 { top: 315px; }
  .kanji-title .k3 { top: 440px; }
  .kanji-title .k4 { top: 572px; }

  .english-title {
    position: absolute;
    top: 726px;
    left: 0;
    width: 100%;
    height: 24px;
    font-size: 20px;
    font-weight: 400;
    letter-spacing: 3px;
  }
  .english-title .word-lead { position: absolute; left: 226px; }
  .english-title .word-tail { position: absolute; left: 455px; color: var(--mist); }
  .c-green { color: var(--t-green); }
  .c-orange { color: var(--t-orange); }
  .c-blue { color: var(--t-blue); }

  .credits {
    position: absolute;
    left: 0;
    top: 1100px;
    width: 100%;
    text-align: center;
    color: var(--credit);
    font-weight: 400;
    text-transform: uppercase;
  }
  .credits .studio { font-size: 12px; letter-spacing: 0.5px; line-height: 18px; }
  .credits .studio small { font-size: 9px; }
  .credits .cast { font-size: 13px; letter-spacing: 0.5px; line-height: 20px; }
  .credits .crew { font-size: 13px; letter-spacing: 0.3px; line-height: 20px; }
  .credits .crew small { font-size: 9px; letter-spacing: 0.5px; margin: 0 3px 0 6px; }
</style>
</head>
<body>
  <main class="poster">
    <h1 class="romaji-title">KAZE <strong>YAMA</strong> TSUKI <strong>HOSHI</strong></h1>

    <div class="gate-scene" role="img" aria-label="Photograph of a young girl in a pink and black kimono standing with her back turned before a wooden temple gate and fence at night"></div>

    <div class="season-strips">
      <div class="strip strip--one" role="img" aria-label="Brush-shaped photo of a traditional Japanese house beside green trees"></div>
      <div class="strip strip--two" role="img" aria-label="Brush-shaped photo of a lake at dusk lined with tall trees"></div>
      <div class="strip strip--three" role="img" aria-label="Brush-shaped photo of red autumn maple leaves"></div>
      <div class="strip strip--four" role="img" aria-label="Brush-shaped photo of a snowy forest in winter"></div>
    </div>

    <h2 class="kanji-title" lang="ja"><span class="k1">風</span><span class="k2">山</span><span class="k3">月</span><span class="k4">星</span></h2>

    <p class="english-title">
      <span class="word-lead"><span class="c-green">T</span><span class="c-orange">H</span><span class="c-blue">E</span></span>
      <span class="word-tail">LANTERNS</span>
    </p>

    <footer class="credits">
      <p class="studio">A TORIIGATA PRODUCTION <small>PRESENT</small></p>
      <p class="cast">ACTOR 01 ACTOR 02 ACTOR 03 ACTOR 04 ACTOR 05 ACTOR 06 ACTOR 03</p>
      <p class="crew"><small>EXECUTIVE PRODUCER</small>NAME SURNAME <small>WRITTEN</small>NAME SURNAME <small>DIRECTED BY</small>NAME SURNAME</p>
    </footer>
  </main>
</body>
</html>
```